Letterhead Design for Law Firm

**Edit: I have added the photo of a bottom that I like.

------
We are looking for a re-design of our new letterhead. The letterhead is for a law firm and will be used for digital and traditionally printed correspondence.

Here are some suggestions:

- Please use colours are #8ec900 and simple black.
- Please do not use any type of "waves" at the bottom of the page. This is not in style at all.
- Please stay modern yet conservative.
- Please use font Segoe UI Light or similar if you can
- Avoid clipart or illustrations.
- Utilize ample white space in the layout so the design looks clean and information is easy to read at a glance. Don't overcrowd the letterhead.
- Make sure the letterhead design is consistent with our brand identity (see harmlane.ca)
-Please, no black headers or footers.

I am attaching my current letterhead and signature for your convenience.

Remember, the letterhead is an extension of our professional identity. We are a successful firm and trial lawyers who correspond with insurers, judges, lawyers, courts, clients, etc. Make it new, modern, attractive, yet powerful and conservative.

It needs to be easily printable. I would like the bleed removed in print so the black bar the bottom crosses the page (but the text is not near the edges)

Target Market(s)

Clients, Government Offices, Judiciary, Lawyers, Insurance Companies, Colleagues.

Industry/Entity Type

Law

Font styles to use
Other font styles liked:
• Segoe UI LIght, Calibri Light,

Colors
00AB8E
00BBA5
67D7C9
C6EFE9
E9F9F6

Requirements
Must have
• Everything that is on the letterhead now.
Nice to have
• Cutting Edge design, yet conservative.
Should not have
• law firm cliche design, images,

```html
<!DOCTYPE html>
<html lang="en">
<head>
<meta charset="utf-8">
<title>Harmlane Letterhead</title>
<link rel="stylesheet" href="https://fonts.googleapis.com/css2?family=Arimo:wght@400;700&family=Nunito+Sans:wght@700&display=swap">
<style>
  :root {
    --brand-green: #8ec900;
    --ink: #111111;
    --text-grey: #555555;
    --rule-grey: #b5b5b5;
    --backdrop: #dcdcdc;
    --paper: #ffffff;
  }
  * { box-sizing: border-box; margin: 0; padding: 0; }
  html, body { width: 1189px; height: 1200px; overflow: hidden; background: var(--backdrop); }
  .letterhead {
    position: absolute; left: 184px; top: 20px;
    width: 820px; height: 1160px;
    background: var(--paper);
    font-family: "Arimo", Arial, sans-serif;
    color: var(--text-grey);
  }
  .brand { position: absolute; left: 73px; top: 50px; width: 220px; text-align: center; }
  .brand-name { font-size: 46px; font-weight: 400; color: var(--ink); letter-spacing: 1px; line-height: 52px; }
  .brand-tagline { font-size: 12px; color: var(--ink); letter-spacing: 1.3px; margin-top: 4px; }
  .divider { position: absolute; top: 58px; width: 1px; height: 52px; background: var(--rule-grey); }
  .divider.first { left: 339px; }
  .divider.second { left: 527px; }
  .contact { position: absolute; left: 381px; top: 62px; list-style: none; font-size: 12.6px; line-height: 15.7px; }
  .contact li { display: flex; align-items: center; gap: 4px; }
  .contact svg { width: 10px; height: 10px; flex: none; }
  .address { position: absolute; left: 563px; top: 62px; font-size: 12.6px; line-height: 15.7px; font-style: normal; }
  .salutation { position: absolute; left: 74px; top: 356px; font-family: "Nunito Sans", sans-serif; font-weight: 700; font-size: 19px; color: var(--text-grey); }
  .body-copy { position: absolute; left: 73px; top: 410px; width: 674px; font-size: 13.8px; line-height: 17px; }
  .body-copy p + p { margin-top: 15px; }
  .closing { position: absolute; left: 74px; top: 760px; font-family: "Nunito Sans", sans-serif; font-weight: 700; font-size: 10px; }
  .signature { position: absolute; left: 73px; top: 808px; width: 134px; height: 40px; background: linear-gradient(90deg, #e6e6e6, #d4d4d4); }
  .footer-band { position: absolute; left: 0; bottom: 0; width: 100%; height: 11px; background: var(--brand-green); }
</style>
</head>
<body>
  <main class="letterhead">
    <header>
      <div class="brand">
        <div class="brand-name">HARMLANE</div>
        <div class="brand-tagline">PERSONAL INJURY LAWYERS</div>
      </div>
      <span class="divider first"></span>
      <ul class="contact">
        <li><svg viewBox="0 0 10 10"><path d="M2 1 L4 1 L4.6 3.2 L3.5 4 Q4.5 6 6 6.5 L6.8 5.4 L9 6 L9 8 Q8.5 9 7 9 Q1 7.5 1 2 Q1 1 2 1 Z" fill="var(--brand-green)"/></svg>905-555-0142</li>
        <li><svg viewBox="0 0 10 10"><rect x="0.5" y="2" width="9" height="6.5" fill="var(--brand-green)"/><path d="M0.5 2 L5 5.6 L9.5 2" stroke="#fff" stroke-width="0.9" fill="none"/></svg>info@harmlane.ca</li>
        <li><svg viewBox="0 0 10 10"><circle cx="5" cy="5" r="4.5" fill="var(--brand-green)"/><path d="M0.5 5 H9.5 M5 0.5 Q2.5 5 5 9.5 M5 0.5 Q7.5 5 5 9.5" stroke="#fff" stroke-width="0.7" fill="none"/></svg>www.harmlane.ca</li>
      </ul>
      <span class="divider second"></span>
      <address class="address">48 Bay Street North<br>Suite 920<br>Hamilton, ON L8R 2P6, Canada</address>
    </header>

    <h1 class="salutation">Dear Mr. Carter,</h1>

    <section class="body-copy">
      <p>Lorem ipsum dolor sit amet, consectetuer adipiscing elit, sed diam nonmmy nibh euismod tincidunt ut laor eet dolore magna aliquam erat volutpat. Ut wisi enim ad minim veniam, quis nostrud exerci tationmcorper suscipit lobortis nisl ut aliquip ex ea commodo consequat. Duis autem vel eum iriure dolor in hendrerit in vulputate velit esse molestie consequat, vel illum dolore eu feugiat</p>
      <p>Rorem ipsum dolor sit amet, consectetuer adipiscing elit, sed diam nonmmy nibh euismod tincidunt ut laor eet dolore magna aliquam erat volutpat. Ut wisi enim ad minim veniam, quis nostrud exerci tationmcorper suscipit lobortis nisl ut aliquip ex ea commodo consequat. Duis autem vel eum iriure dolor in hendrerit in vulputate velit esse molest</p>
      <p>Dorem ipsum dolor sit amet, consectetuer adipiscing elit, sed diam nonmmy nibh euismod tincidunt ut laor eet dolore magna aliquam erat volutpat. Ut wisi enim ad minim veniam, quis nostrud exerci tationmcorper suscipit lobortis nisl ut aliquip ex ea commodo consequat. Duis autem vel eum iriure dolor in hendrerit in suscipit lobortis nisl ut aliquip ex ea commodo consequat. Duis autem vel eum iriure dolor in hendrerit in vulputate velit esse molestie consequat, vel illum</p>
      <p>Sorem ipsum dolor sit amet, consectetuer adipiscing elit, sed diam nonmmy nibh euismod tincidunt ut laor eet dolore magna aliquam erat volutpat. Ut wisi enim ad minim veniam, quis nostrud exerci tationmcorper suscipit lobortis nisl ut aliquip ex ea commodo consequat. Duis autem vel eum iriure dolor in</p>
    </section>

    <p class="closing">Sincerely,</p>
    <div class="signature" role="img" aria-label="Handwritten signature of the sender"></div>

    <div class="footer-band"></div>
  </main>
</body>
</html>
```